Pale Lantern Double Sided Flyer Design

We need a double sided flyer (1/3 of an A4 which is 99mm x 210mm) developed for our Newcastle(NSW) tour. This flyer will be placed in tourist information centres and hotels. We want it to direct people to our website or be able to make bookings over the phone.

About Us:-
We are a city walking tour company that runs tours day or night. We run both day and night and will incorporate real history / real PALE LANTERN. Some of the stories will be quite serious i.e.- there are infamous murders from 100 years ago, baffling court cases, even a bit of poetry written by murderers, suicides, love triangles, you name it. We will be telling the historical stories that tourists will not hear from any other tour provider. A bit of darkness, a bit of mystery and a bit of history theme.

We do no go for scares and let the very real stories deliver the entertainment for our guests. Our customers enjoy our tours, but it isn't light fun and frivolity. Our stories are being carefully crafted and are packed with unexpected twists, turns; revelations whilst remaining all 100% true. We deliver deep, rich, engaging stories.

Here are a few samples of quotes from the characters in our stories that may give you an idea of the kind of history we will cover:-

"There were bits of spines, bits of skulls, [and] finger bones spilled out all over the streets - I ended up filling three boxes. Children were playing with them for weeks”

"I had a close shave last night and now I want a close haircut.”

“She's a beautiful child', isn't she? She's the cause of all the trouble.”

“I did it because she would not come home with me.”

"I have killed my wife. I’m glad she’s dead.”

"Stand aside or I'll put a bullet through both of you."

“You villain, I'll teach you to take away my character."

“You’re not dead yet, you bastard!”

Our website, booking form and contact details can be viewed at www.palelantern.com.au

Target Market(s)

Tourists

Industry/Entity Type

Tour

Colors

Designer to choose colors to be used in the design.

Requirements
Must have
• Vertical orientation please.
• Please also include a reference to a discount offer of 25% using the promo code "WICK".
Nice to have
• FRONT FLYER INFORMATION
• - Pale Lantern Logo
• - "I have killed my wife; I'm glad she's dead."
• - Harbourside Hidden Lanes Walk
• - 25% Discount Offer Codeword WICK
• - web address at the base; www.palelantern.com.au
• BACK FLYER INFORMATION
• - "She's a beautiful child', isn't she? She's the cause of all the trouble.
• - Pale Lantern Logo at the base along with the web address www.palelantern.com.au
• - Blurb:- Pale lantern brings back Newcastle's hidden past, the forgotten past, the dark past that may not want to be remembered.
• Real stories from the streets around you. Discover the histories you won't hear anywhere else. The forgotten stories of yesteryear finally get a chance to be told. Through you they get to live again.
Should not have
• GENERAL
• Please do not include the phone number, email address or social media icons. We want to drive online bookings.

```html
<!DOCTYPE html>
<html lang="en">
<head>
<meta charset="utf-8">
<title>Pale Lantern Walking Tours – Flyer Presentation</title>
<link rel="stylesheet" href="https://fonts.googleapis.com/css2?family=Great+Vibes&family=Tinos:wght@400;700&display=swap">
<style>
  :root {
    --board-bg: #050505;
    --board-haze: #1c1c1c;
    --cream: #f4e5bf;
    --red-light: #8e2417;
    --red-mid: #6c160d;
    --red-deep: #3a0805;
    --parchment: #e4c995;
    --parchment-edge: #c9a66a;
    --ink: #2b1a0e;
    --frame-line: rgba(236, 210, 160, 0.45);
    --ornament: rgba(226, 196, 140, 0.35);
    --photo-dark: #1d1d1d;
    --photo-light: #6b6b6b;
  }
  * { box-sizing: border-box; margin: 0; padding: 0; }
  html, body { width: 1200px; height: 821px; overflow: hidden; background: var(--board-bg); }
  .board {
    position: relative; width: 1200px; height: 821px; overflow: hidden;
    font-family: "Tinos", "Times New Roman", serif; color: var(--cream);
  }
  .board-backdrop {
    position: absolute; inset: 0;
    background: radial-gradient(ellipse at 78% 55%, var(--board-haze) 0%, var(--board-bg) 70%);
  }
  .side-label { position: absolute; font-size: 40px; line-height: 1; color: var(--cream); text-align: center; width: 200px; }
  .side-label--back { left: 449px; top: 100px; }
  .side-label--front { left: 130px; top: 698px; }

  .flyer {
    position: absolute; overflow: hidden;
    background: radial-gradient(ellipse at 50% 45%, var(--red-light) 0%, var(--red-mid) 55%, var(--red-deep) 100%);
    box-shadow: 0 0 0 2px #000;
  }
  .flyer--front { left: 103px; top: 101px; width: 259px; height: 561px; }
  .flyer--back { left: 415px; top: 165px; width: 267px; height: 581px; }
  .flyer-frame { position: absolute; inset: 8px; border: 1px solid var(--frame-line); }
  .corner-ornament { position: absolute; width: 30px; height: 30px; background: var(--ornament); }
  .corner-ornament--tl { left: 4px; top: 4px; }
  .corner-ornament--tr { right: 4px; top: 4px; }
  .corner-ornament--bl { left: 4px; bottom: 4px; }
  .corner-ornament--br { right: 4px; bottom: 4px; }

  .script { font-family: "Great Vibes", "Brush Script MT", cursive; color: var(--cream); text-align: center; position: absolute; left: 0; right: 0; line-height: 1; }
  .front-kicker { top: 24px; font-size: 22px; }
  .front-title { top: 58px; font-size: 40px; }
  .medallion-ornament {
    position: absolute; left: 12px; top: 112px; width: 235px; height: 160px;
    background: radial-gradient(ellipse at center, rgba(230,200,150,0.45) 0%, rgba(230,200,150,0.15) 60%, transparent 75%);
  }
  .medallion-photo {
    position: absolute; left: 78px; top: 140px; width: 102px; height: 90px; border-radius: 50%;
    background: radial-gradient(circle at 50% 60%, var(--photo-light) 0%, var(--photo-dark) 75%);
    box-shadow: 0 0 0 3px var(--parchment-edge);
  }
  .contact-card {
    position: absolute; left: 27px; top: 312px; width: 207px; height: 128px;
    background: linear-gradient(180deg, var(--parchment) 0%, #dcbd84 100%);
    color: var(--ink); text-align: center; border: 1px solid var(--parchment-edge);
  }
  .contact-card__heading { margin-top: 6px; font-size: 18px; line-height: 1.05; }
  .contact-card__offer { font-size: 14px; line-height: 1.05; }
  .contact-card__rule { height: 2px; background: var(--ink); margin: 7px 0 10px; }
  .contact-card__line { font-size: 14px; line-height: 1.35; }
  .front-tagline { top: 472px; font-size: 21px; line-height: 1.05; }

  .brand-name {
    position: absolute; text-align: center; font-weight: 700; color: var(--cream);
    white-space: nowrap; line-height: 1;
  }
  .brand-mark { display: inline-block; background: var(--cream); }
  .brand-name--back { left: 0; right: 0; top: 112px; font-size: 24px; letter-spacing: 0.5px; }
  .brand-name--back .brand-mark { width: 11px; height: 11px; margin-right: 7px; vertical-align: 2px; }
  .back-blurb {
    position: absolute; left: 16px; right: 16px; top: 152px; text-align: center;
    font-size: 12px; line-height: 15.5px; color: var(--cream);
  }
  .back-blurb p + p { margin-top: 15.5px; }
  .back-kicker { top: 462px; font-size: 20px; }
  .back-title { top: 486px; font-size: 32px; }
  .back-contact { position: absolute; left: 0; right: 0; top: 532px; text-align: center; font-size: 14px; line-height: 19px; }

  .spec { position: absolute; left: 720px; width: 450px; text-align: center; }
  .spec-brand { top: 242px; font-size: 40px; font-weight: 700; letter-spacing: 1px; }
  .spec-brand .brand-mark { width: 18px; height: 18px; margin-right: 10px; vertical-align: 5px; }
  .spec-notes { top: 306px; font-size: 25px; line-height: 33.5px; color: var(--cream); }
  .spec-notes p + p { margin-top: 33.5px; }
</style>
</head>
<body>
<main class="board">
  <div class="board-backdrop" role="img" aria-label="Darkened city streetscape backdrop"></div>

  <div class="side-label side-label--back">Back</div>
  <div class="side-label side-label--front">Front</div>

  <section class="flyer flyer--front" aria-label="Flyer front">
    <div class="flyer-frame"></div>
    <div class="corner-ornament corner-ornament--tl" role="img" aria-label="Corner flourish"></div>
    <div class="corner-ornament corner-ornament--tr" role="img" aria-label="Corner flourish"></div>
    <div class="corner-ornament corner-ornament--bl" role="img" aria-label="Corner flourish"></div>
    <div class="corner-ornament corner-ornament--br" role="img" aria-label="Corner flourish"></div>

    <div class="script front-kicker">Pale Lantern</div>
    <div class="script front-title">Walking Tours</div>

    <div class="medallion-ornament" role="img" aria-label="Ornate gilded frame flourish"></div>
    <div class="medallion-photo" role="img" aria-label="Black and white photo of an old tram at night"></div>

    <div class="contact-card">
      <div class="contact-card__heading">BOOK ONLINE TODAY</div>
      <div class="contact-card__offer">25% off with<br>promo code “WICK”</div>
      <div class="contact-card__rule"></div>
      <div class="contact-card__line">Bookings online at</div>
      <div class="contact-card__line">www.palelantern.com.au</div>
    </div>

    <div class="script front-tagline">compelling reminders of<br>the amazing times<br>that precede us</div>
  </section>

  <section class="flyer flyer--back" aria-label="Flyer back">
    <div class="flyer-frame"></div>
    <div class="corner-ornament corner-ornament--tl" role="img" aria-label="Corner flourish"></div>
    <div class="corner-ornament corner-ornament--tr" role="img" aria-label="Corner flourish"></div>
    <div class="corner-ornament corner-ornament--bl" role="img" aria-label="Corner flourish"></div>
    <div class="corner-ornament corner-ornament--br" role="img" aria-label="Corner flourish"></div>

    <div class="brand-name brand-name--back"><span class="brand-mark"></span>PALE LANTERN</div>

    <div class="back-blurb">
      <p>Newcastle's Pale Lantern<br>have been forgotten....until now.<br>Rediscover the dark past of the city streets.<br>Take this unique walking tour to learn about<br>the all too real stories that make<br>up a cities past.</p>
      <p>Duration: 90 Minutes (approx.)</p>
      <p>Some of these stories may be tales of dark<br>things.....some may simply be a charming<br>reminder of days gone by.....these stories are<br>compelling reminders of the amazing times<br>that precede us.....and the forgotten people of<br>yesteryear finally get a chance to have their<br>story told. Through you, the often dark lives<br>of the people of yesterday get to live again.<br>Will you like what you hear?</p>
    </div>

    <div class="script back-kicker">Forgotten History</div>
    <div class="script back-title">Walking Tours</div>

    <div class="back-contact">Book your tour online at<br>www.palelantern.com.au</div>
  </section>

  <div class="spec spec-brand brand-name"><span class="brand-mark"></span>PALE LANTERN</div>
  <div class="spec spec-notes">
    <p>Two sided flyer<br>99mm by 210mm<br>High Quality 300dpi<br>Print Ready</p>
    <p>All text is editable<br>and basic revisions are free</p>
    <p>If you have any questions<br>I am always available<br>to answer them</p>
  </div>
</main>
</body>
</html>
```